Business Card Design Project

Hi,
I am after a business card design for a new business. The business is called Quarrel Works and is a stockist of building supplies used for modern cosmetic renovations for houses. (e.g Floorboards, timber decking, modern fittings and fixtures.)
The logo and font faces have been attached.
The logo comes in 2 different color scheme's - 1. Orange on White & 2. Orange on Black. I would like 2 versions of the business card design to reflect these color scheme's.
The designs need to be double sided. The front should contain all the contact information, whilst the back of the card should display the logo and the URL of the webpage - www.quarrelworks-demo.com.au . The logo needs to be displayed creatively on the back of the card.
The business card design needs to reflect the image of modern living, but should also have the wow factor.

```html
<!DOCTYPE html>
<html lang="en">
<head>
<meta charset="utf-8">
<title>Quarrel Works – Business Cards</title>
<link rel="stylesheet" href="https://fonts.googleapis.com/css2?family=Roboto:wght@300;400&display=swap">
<style>
  :root {
    --orange: #e8621d;
    --rust: #a9431f;
    --ink: #231f20;
    --paper: #ffffff;
    --grey: #555555;
    --edge: #333333;
  }
  * { margin: 0; padding: 0; box-sizing: border-box; }
  html, body { width: 1200px; height: 843px; overflow: hidden; background: var(--paper); }
  body { position: relative; font-family: "Roboto", Arial, sans-serif; font-weight: 300; }

  .card {
    position: absolute;
    width: 495px;
    height: 325px;
    border-radius: 32px;
    overflow: hidden;
  }
  .card--light { background: var(--paper); border: 1px solid var(--edge); }
  .card--dark { background: var(--ink); }

  .back-light { left: 96px; top: 85px; }
  .front-light { left: 621px; top: 85px; }
  .back-dark { left: 96px; top: 439px; }
  .front-dark { left: 621px; top: 439px; }

  /* brand name lockup */
  .brand { position: absolute; display: flex; align-items: center; gap: 12px; }
  .brand__square { background: var(--orange); flex: none; }
  .brand__name { color: var(--orange); font-weight: 400; white-space: nowrap; }

  .back .brand { left: 50%; top: 118px; transform: translateX(-50%); }
  .back .brand__square { width: 44px; height: 44px; }
  .back .brand__name { font-size: 40px; }

  .url-band {
    position: absolute; left: 0; right: 0; top: 197px; height: 28px;
    background: var(--orange);
    color: var(--paper);
    font-size: 19px;
    text-align: center;
    line-height: 28px;
  }

  .front .brand { left: 34px; top: 32px; gap: 9px; }
  .front .brand__square { width: 28px; height: 28px; }
  .front .brand__name { font-size: 26px; }

  .person { position: absolute; left: 35px; top: 135px; }
  .person__name { color: var(--orange); font-size: 37px; font-weight: 300; line-height: 1; }
  .person__role {
    margin-top: 12px; font-size: 13px; letter-spacing: 2.2px; text-transform: uppercase;
    color: var(--grey);
  }
  .card--dark .person__role { color: #e6e6e6; }

  .contact { position: absolute; left: 35px; top: 228px; list-style: none; font-size: 13px; line-height: 17px; color: var(--grey); }
  .card--dark .contact { color: #e6e6e6; }

  .pattern-panel {
    position: absolute; right: 0; top: 0; bottom: 0; width: 172px;
    background: linear-gradient(135deg, var(--orange) 0%, var(--rust) 55%, var(--orange) 100%);
  }
</style>
</head>
<body>

  <section class="card card--light back back-light">
    <div class="brand">
      <span class="brand__square"></span>
      <span class="brand__name">Quarrel Works</span>
    </div>
    <div class="url-band">www.quarrelworks-demo.com.au</div>
  </section>

  <section class="card card--light front front-light">
    <div class="brand">
      <span class="brand__square"></span>
      <span class="brand__name">Quarrel Works</span>
    </div>
    <div class="person">
      <p class="person__name">Dana Marlow</p>
      <p class="person__role">Managing Director</p>
    </div>
    <ul class="contact">
      <li>A: 42 Alder Lane, Hamilton, Canada</li>
      <li>P: 555 014 2290</li>
      <li>M: 555 019 7734</li>
      <li>E: hello@quarrelworks-demo.com</li>
    </ul>
    <div class="pattern-panel" role="img" aria-label="Decorative pattern of orange and rust tiles with white corner outlines"></div>
  </section>

  <section class="card card--dark back back-dark">
    <div class="brand">
      <span class="brand__square"></span>
      <span class="brand__name">Quarrel Works</span>
    </div>
    <div class="url-band">www.quarrelworks-demo.com.au</div>
  </section>

  <section class="card card--dark front front-dark">
    <div class="brand">
      <span class="brand__square"></span>
      <span class="brand__name">Quarrel Works</span>
    </div>
    <div class="person">
      <p class="person__name">Dana Marlow</p>
      <p class="person__role">Managing Director</p>
    </div>
    <ul class="contact">
      <li>A: 42 Alder Lane, Hamilton, Canada</li>
      <li>P: 555 014 2290</li>
      <li>M: 555 019 7734</li>
      <li>E: hello@quarrelworks-demo.com</li>
    </ul>
    <div class="pattern-panel" role="img" aria-label="Decorative pattern of orange and rust tiles with black corner outlines"></div>
  </section>

</body>
</html>
```